Etiketten-Design für Gin
Zielgruppe
Herstellung von Spirituosen/ Molk UG (haftungsbeschränkt)
Zielgruppe: Vorwiegend Männer von 45 bis 70 Jahre
Aufgabenstellung
Flaschen Etikett Vorder- und Rückseite für Gin
Wortmarke: Dry Gin Molk sollte hervorgehoben sein.
Bedeutung hat für uns auch, dass er aus der Region Rhein-Main kommt.

```html
<!DOCTYPE html>
<html lang="de">
<head>
<meta charset="utf-8">
<title>Dry Gin Molk – Etiketten Vorder- und Rückseite</title>
<link rel="stylesheet" href="https://fonts.googleapis.com/css2?family=Smokum&family=Alfa+Slab+One&family=Oswald:wght@600&display=swap">
<style>
  :root {
    --label-bg: #303030;
    --gold: #948463;
    --page-bg: #ffffff;
  }
  html, body {
    margin: 0;
    padding: 0;
    width: 1200px;
    height: 748px;
    overflow: hidden;
    background: var(--page-bg);
  }
  .canvas {
    position: relative;
    width: 1200px;
    height: 748px;
  }
  .label {
    position: absolute;
    top: 78px;
    width: 284px;
    height: 594px;
    background: var(--label-bg);
  }
  .label--front { left: 212px; }
  .label--back { left: 716px; }
  .label svg { display: block; width: 284px; height: 594px; overflow: visible; }
  .rule { stroke: var(--gold); stroke-width: 2; fill: none; }
  .rule--thin { stroke-width: 1.4; }
  .ink { fill: var(--gold); }
  .display { font-family: "Smokum", "Oswald", sans-serif; }
  .slab { font-family: "Alfa Slab One", "Rockwell", serif; }
  .condensed { font-family: "Oswald", "Arial Narrow", sans-serif; font-weight: 600; }
</style>
</head>
<body>
<main class="canvas">

  <!-- Vorderseite -->
  <section class="label label--front" aria-label="Etikett Vorderseite">
    <svg viewBox="0 0 284 594" xmlns="http://www.w3.org/2000/svg">
      <defs>
        <path id="front-brand-arc" d="M 30 150 Q 146 72 262 150"/>
        <path id="front-origin-arc" d="M 62 408 Q 144 452 226 406"/>
      </defs>

      <g class="brand-arch">
        <path class="rule" d="M 17 118 Q 146 2 275 118"/>
        <text class="display ink" font-size="40">
          <textPath href="#front-brand-arc" startOffset="1" textLength="246" lengthAdjust="spacingAndGlyphs">DESTILLERIE MOLK</textPath>
        </text>
        <path class="rule" d="M 64 161 Q 146 87 227 161"/>
      </g>

      <g class="wordmark">
        <text class="display ink" x="16" y="310" font-size="118" textLength="258" lengthAdjust="spacingAndGlyphs">DRY GIN MOLK</text>
        <line class="rule" x1="10" y1="313" x2="274" y2="313"/>
      </g>

      <polygon class="ink divider" points="143,353 151,367 143,382 135,367"/>

      <text class="display ink origin" font-size="28">
        <textPath href="#front-origin-arc" startOffset="1" textLength="168" lengthAdjust="spacingAndGlyphs">DISTILLED IN GERMANY</textPath>
      </text>

      <g class="info-bar">
        <line class="rule" x1="11" y1="517" x2="273" y2="517"/>
        <line class="rule" x1="11" y1="556" x2="273" y2="556"/>
        <line class="rule" x1="11" y1="527" x2="51" y2="527"/>
        <line class="rule" x1="11" y1="537" x2="51" y2="537"/>
        <line class="rule" x1="11" y1="547" x2="51" y2="547"/>
        <line class="rule" x1="233" y1="527" x2="273" y2="527"/>
        <line class="rule" x1="233" y1="537" x2="273" y2="537"/>
        <line class="rule" x1="233" y1="547" x2="273" y2="547"/>
        <text class="display ink" x="63" y="549" font-size="28" textLength="32" lengthAdjust="spacingAndGlyphs">35 CL</text>
        <polygon class="ink" points="143,527 149,537 143,548 137,537"/>
        <text class="display ink" x="176" y="548" font-size="28" textLength="52" lengthAdjust="spacingAndGlyphs">45 % VOL.</text>
      </g>
    </svg>
  </section>

  <!-- Rückseite -->
  <section class="label label--back" aria-label="Etikett Rückseite">
    <svg viewBox="0 0 284 594" xmlns="http://www.w3.org/2000/svg">
      <defs>
        <path id="back-brand-arc" d="M 37 104 Q 150 36 264 104"/>
      </defs>

      <g class="brand-arch">
        <path class="rule" d="M 20 75 Q 143 -35 267 75"/>
        <text class="display ink" font-size="38">
          <textPath href="#back-brand-arc" startOffset="1" textLength="236" lengthAdjust="spacingAndGlyphs">DESTILLERIE MOLK</textPath>
        </text>
        <path class="rule" d="M 66 116 Q 143 46 221 116"/>
      </g>

      <g class="wordmark">
        <polygon class="ink" points="49,145 54,153 49,162 44,153"/>
        <text class="display ink" x="88" y="174" font-size="54" textLength="120" lengthAdjust="spacingAndGlyphs">DRY GIN MOLK</text>
        <line class="rule rule--thin" x1="86" y1="176" x2="208" y2="176"/>
        <polygon class="ink" points="248,145 253,153 248,162 243,153"/>
        <text class="display ink" x="147" y="205" font-size="22" text-anchor="middle" textLength="74" lengthAdjust="spacingAndGlyphs">WESTERN DRY GIN</text>
      </g>

      <g class="description slab ink" font-size="18" text-anchor="middle">
        <text x="143" y="247" textLength="208" lengthAdjust="spacingAndGlyphs">EIN ERLESENER GIN AUS</text>
        <text x="143" y="274" textLength="146" lengthAdjust="spacingAndGlyphs">DEM HERZEN DES</text>
        <text x="143" y="300" textLength="222" lengthAdjust="spacingAndGlyphs">RHEIN-MAIN GEBIETES, IM</text>
        <text x="143" y="327" textLength="200" lengthAdjust="spacingAndGlyphs">KUPFERKESSEL 2-FACH</text>
        <text x="143" y="353" textLength="118" lengthAdjust="spacingAndGlyphs">DESTILLIERT.</text>
        <text x="143" y="380" textLength="210" lengthAdjust="spacingAndGlyphs">ER SCHMECKT DEUTLICH</text>
        <text x="143" y="406" textLength="242" lengthAdjust="spacingAndGlyphs">NACH ZITRUSNOTEN, LEICHT</text>
        <text x="143" y="433" textLength="208" lengthAdjust="spacingAndGlyphs">PFEFFRIG UND ENTHÄLT</text>
        <text x="143" y="459" textLength="242" lengthAdjust="spacingAndGlyphs">SUBTIL HERBE BOTANICALS.</text>
      </g>

      <g class="legal condensed ink" text-anchor="middle">
        <text x="145" y="491" font-size="15" textLength="240" lengthAdjust="spacingAndGlyphs">Destilliert und abgefüllt in Deutschland.</text>
        <text x="145" y="504" font-size="9" textLength="240" lengthAdjust="spacingAndGlyphs">Erzeugerbetrieb: Molk UG (haftungsbeschränkt), D-63999 Kesselbach</text>
      </g>

      <g class="info-bar">
        <line class="rule" x1="11" y1="518" x2="90" y2="518"/>
        <line class="rule" x1="11" y1="556" x2="90" y2="556"/>
        <line class="rule" x1="195" y1="518" x2="274" y2="518"/>
        <line class="rule" x1="195" y1="556" x2="274" y2="556"/>
        <line class="rule" x1="11" y1="528" x2="40" y2="528"/>
        <line class="rule" x1="11" y1="537" x2="40" y2="537"/>
        <line class="rule" x1="11" y1="547" x2="40" y2="547"/>
        <line class="rule" x1="245" y1="528" x2="274" y2="528"/>
        <line class="rule" x1="245" y1="537" x2="274" y2="537"/>
        <line class="rule" x1="245" y1="547" x2="274" y2="547"/>
        <text class="condensed ink" x="48" y="543" font-size="13">35 cl</text>
        <rect class="ink code-field" x="94" y="512" width="97" height="51"/>
        <text class="condensed ink" x="199" y="542" font-size="12" textLength="42" lengthAdjust="spacingAndGlyphs">45 % Vol.</text>
      </g>
    </svg>
  </section>

</main>
</body>
</html>
```